Business Card for Multi-Brand Sportswear Company

We are looking for a business card which represents our company and the multiple brands within it.

The company: Kelt Athletic (LTD)
The brands: Kelt, PawaLuni, VerdantFlex, Grit and Gale

Employees using these cards would be representing Kelt Athletic, rather than any of the individual brands. You will see a current design within the uploaded files, to give some inspiration. The actual text of the brands is not necessary, but the logos should be on there is some format.

Our creative minds on this are stretched, so we are looking for someone to make this their own, and show us what a good business card should look like.

We may like to get these printed with spot gloss, so keep that in mind with your designs.

www.keltathletic.co.uk

Industry/Entity Type

Business

Contact Information for Business Card

Tom Hollingsworth-Pryce
Operations Manager
(+44) 1632 960 418
Tom@keltathletic.co.uk
www.keltathletic.co.uk

Font styles to use
Sans Serif
Other font styles liked:
• Eurostile

Colors
ffffff

Requirements
Nice to have
• Dark (black) background

```html
<!DOCTYPE html>
<html lang="en">
<head>
<meta charset="utf-8">
<title>Kelt Athletic – Business Card</title>
<link rel="stylesheet" href="https://fonts.googleapis.com/css2?family=Michroma&family=Rajdhani:wght@500;600&display=swap">
<style>
  :root {
    --page: #e9e9e7;
    --card: #0d0d0f;
    --tone-grey: #2a2a2e;
    --red: #e8392b;
    --red-deep: #5a1712;
    --white: #ffffff;
    --muted: #d8d8d8;
  }
  html, body {
    margin: 0;
    width: 891px;
    height: 1200px;
    overflow: hidden;
    background: var(--page);
  }
  .card {
    position: absolute;
    left: 82px;
    width: 733px;
    height: 478px;
    display: block;
    box-shadow: 0 4px 14px rgba(0,0,0,0.25);
  }
  .card--front { top: 70px; }
  .card--back { top: 665px; }
  .card-base { fill: var(--card); }
  .accent-band { fill: var(--red); }
  .brand-row { font-family: "Michroma", sans-serif; font-size: 6.5px; fill: var(--white); }
  .wordmark { font-family: "Rajdhani", sans-serif; font-weight: 600; fill: var(--white); letter-spacing: 0.5px; }
  .tagline { font-family: "Rajdhani", sans-serif; font-weight: 500; fill: var(--white); letter-spacing: 1.2px; }
  .contact { font-family: "Michroma", sans-serif; font-size: 8.4px; fill: var(--white); }
  .contact-icon { fill: var(--white); }
  .contact-glyph { fill: none; stroke: var(--card); stroke-width: 1; }
  .person-name { font-family: "Michroma", sans-serif; font-size: 9.4px; fill: var(--muted); letter-spacing: 0.6px; }
  .person-role { font-family: "Michroma", sans-serif; font-size: 7.2px; fill: var(--muted); letter-spacing: 0.6px; }
</style>
</head>
<body>

<svg class="card card--front" viewBox="0 0 502 327" aria-label="Business card front">
  <defs>
    <linearGradient id="front-tone" x1="0" y1="0" x2="1" y2="0">
      <stop offset="0" stop-color="var(--tone-grey)"/>
      <stop offset="1" stop-color="var(--card)"/>
    </linearGradient>
    <linearGradient id="accent-tone" x1="0" y1="0" x2="1" y2="0">
      <stop offset="0" stop-color="var(--red-deep)"/>
      <stop offset="1" stop-color="var(--card)"/>
    </linearGradient>
  </defs>
  <rect class="card-base" width="502" height="327"/>
  <rect x="0" y="0" width="200" height="327" fill="url(#front-tone)" role="img" aria-label="Glossy decorative panel"/>
  <rect x="136" y="80" width="366" height="84" fill="url(#accent-tone)" role="img" aria-label="Red decorative accent"/>

  <text class="brand-row" x="484" y="30" text-anchor="end">
    <tspan>PawaLuni</tspan><tspan dx="14">VerdantFlex</tspan><tspan dx="14">Kelt</tspan><tspan dx="14">Grit and Gale</tspan>
  </text>

  <text class="wordmark" x="484" y="128" font-size="17" text-anchor="end">KELT ATHLETIC</text>
  <text class="tagline" x="484" y="137" font-size="5" text-anchor="end">PERFORMANCE WEAR</text>

  <g class="contact-list">
    <circle class="contact-icon" cx="21" cy="245" r="5"/>
    <path class="contact-glyph" d="M18,243 h6 v4 h-6 z M18,243 l3,2 l3,-2"/>
    <text class="contact" x="33" y="248">Tom@keltathletic.co.uk</text>

    <circle class="contact-icon" cx="21" cy="270" r="5"/>
    <path class="contact-glyph" d="M19,267.5 q0,4 4,5"/>
    <text class="contact" x="33" y="273">(+44) 1632 960 418</text>

    <circle class="contact-icon" cx="21" cy="294" r="5"/>
    <path class="contact-glyph" d="M16,294 h10 M21,289 q-3,5 0,10 M21,289 q3,5 0,10"/>
    <text class="contact" x="33" y="297">www.keltathletic.co.uk</text>
  </g>

  <text class="person-name" x="484" y="247" text-anchor="end">Tom Hollingsworth-Pryce</text>
  <text class="person-role" x="484" y="263" text-anchor="end">Operations Manager</text>
</svg>

<svg class="card card--back" viewBox="0 0 502 327" aria-label="Business card back">
  <defs>
    <linearGradient id="back-tone" x1="0" y1="0" x2="1" y2="1">
      <stop offset="0" stop-color="var(--tone-grey)"/>
      <stop offset="1" stop-color="var(--card)"/>
    </linearGradient>
  </defs>
  <rect class="card-base" width="502" height="327"/>
  <rect x="0" y="0" width="170" height="300" fill="url(#back-tone)" role="img" aria-label="Glossy decorative panel"/>

  <text class="wordmark" x="250" y="180" font-size="38" text-anchor="middle">KELT ATHLETIC</text>
  <text class="tagline" x="250" y="194" font-size="9" text-anchor="middle">PERFORMANCE WEAR</text>

  <rect class="accent-band" x="0" y="307" width="502" height="20"/>
</svg>

</body>
</html>
```